Pediatric Dental Practice needs a postcard for direct mail advertising

We are looking for a creative and professional double-sided postcard design for a direct mail marketing campaign. Our goal is to attract new families to our pediatric dental practice by conveying a sense of warmth, modern care, and clinical excellence. The design should feel "boutique" and high-end yet remain fun and approachable for parents and children.

```html
<!DOCTYPE html>
<html lang="en">
<head>
<meta charset="utf-8">
<title>Maple Grove Pediatric Dentistry – Postcard</title>
<link href="https://fonts.googleapis.com/css2?family=Poppins:wght@400;500;600;700;800&family=Arimo:wght@400&display=swap" rel="stylesheet">
<style>
:root{
  --stage:#939497;
  --sage:#9dba91;
  --sage-light:#c4dcb8;
  --sage-dark:#6f9a63;
  --forest:#2d5a27;
  --forest-btn:#2f7a3a;
  --ink:#262626;
  --cream:#fcf8f1;
  --white:#ffffff;
  --mint:#e9f3e3;
}
*{box-sizing:border-box;margin:0;padding:0}
html,body{width:836px;height:1200px;overflow:hidden}
body{background:var(--stage);font-family:'Poppins',sans-serif;color:var(--ink);position:relative}
.card{position:absolute;left:92px;width:651px;height:421px;overflow:hidden}
.card-front{top:154px;background:linear-gradient(120deg,var(--sage) 55%,var(--sage-light))}
.card-back{top:640px;background:linear-gradient(100deg,#efe9df 0%,#f1f4ec 45%,var(--mint) 100%)}
.abs{position:absolute}
.wave{position:absolute;left:0;width:651px}

/* brand */
.brand-dot{border-radius:50%;background:var(--forest-btn)}
.brand-name{font-weight:500;color:var(--ink);line-height:1;white-space:nowrap}
.brand-tag{font-weight:500;color:var(--ink);letter-spacing:.32em;white-space:nowrap}

/* front */
.headline{font-weight:800;font-size:38px;line-height:1;letter-spacing:-.5px;white-space:nowrap}
.headline-light{color:var(--white)}
.headline-dark{color:var(--forest)}
.lede{font-size:13px;line-height:18px;color:var(--ink)}
.lede strong{color:var(--forest);font-weight:700}
.feature{width:100px;text-align:center}
.feature-badge{width:42px;height:42px;margin:0 auto 6px;border-radius:50%;background:var(--cream);display:flex;align-items:center;justify-content:center}
.feature-label{font-size:8.6px;line-height:12px;color:#333}
.hero-photo{left:357px;top:16px;width:290px;height:304px}

/* back */
.back-title{font-weight:700;font-size:30px;color:var(--forest);letter-spacing:-.5px;line-height:1}
.back-sub{font-weight:600;font-size:21px;color:var(--ink);line-height:1}
.back-intro{font-size:10px;line-height:13px;color:var(--ink)}
.back-intro em{font-style:normal;font-weight:600;color:var(--sage-dark)}
.stamp{left:560px;top:42px;width:68px;height:68px;background:var(--white);border:1px solid #c7d2c7}
.dentist-photo{left:17px;top:141px;width:175px;height:225px;border-radius:4px;background:linear-gradient(180deg,#d8cbbd,#a9c3e0 60%,#8fb0d6)}
.meet{font-weight:600;font-size:18px;line-height:21px;color:var(--ink)}
.name-btn{left:199px;top:197px;width:161px;height:32px;background:var(--forest-btn);border-radius:3px;color:var(--white);font-weight:500;font-size:14px;display:flex;align-items:center;gap:7px;padding-left:11px}
.bio{left:205px;top:244px;width:165px;font-family:'Arimo',sans-serif;font-size:9.4px;line-height:10.6px;color:var(--ink)}

/* contact bar */
.contact{position:absolute;left:0;top:374px;width:651px;height:40px;font-size:11px;color:var(--ink)}
.contact .pin-ico{position:absolute;width:18px;height:18px;border-radius:50%;background:var(--forest-btn);display:flex;align-items:center;justify-content:center}
.phone-num{position:absolute;left:52px;top:9px;font-weight:600;font-size:13.5px}
.web{position:absolute;left:176px;top:4px;font-size:9.6px;line-height:11px;font-weight:500}
.web span{display:block;position:relative;padding-left:11px}
.web span::before{content:"";position:absolute;left:0;top:4px;width:5px;height:4px;background:var(--forest-btn)}
.addr{position:absolute;left:388px;top:4px;font-size:9.6px;line-height:10.5px;font-weight:500}
</style>
</head>
<body>

<!-- FRONT -->
<section class="card card-front">
  <div class="abs brand-dot" style="left:38px;top:41px;width:26px;height:26px"></div>
  <div class="abs brand-name" style="left:102px;top:42px;font-size:26px">maple grove</div>
  <div class="abs brand-tag" style="left:103px;top:73px;font-size:10px">PEDIATRIC DENTISTRY</div>

  <div class="abs headline headline-light" style="left:45px;top:114px">HAPPY VISITS.</div>
  <div class="abs headline headline-dark" style="left:45px;top:153px">HEALTHY SMILES.</div>
  <svg class="abs" style="left:45px;top:186px" width="92" height="12" viewBox="0 0 92 12"><path d="M3 9 Q40 2 89 4" stroke="#fff" stroke-width="4" fill="none" stroke-linecap="round"/></svg>

  <p class="abs lede" style="left:50px;top:210px;width:320px">Compassionate, expert dental care<br>for children in a <strong>warm, modern environment.</strong></p>

  <div class="abs feature" style="left:42px;top:256px">
    <div class="feature-badge"><svg width="22" height="22" viewBox="0 0 24 24" fill="none" stroke="#333" stroke-width="1.4"><path d="M7 3c-3 0-4 3-3.5 6 .5 3 1.5 4 2 8 .3 3 2 3 2.5 0l1-4c.4-1.5 2.6-1.5 3 0l1 4c.5 3 2.2 3 2.5 0 .5-4 1.5-5 2-8 .5-3-.5-6-3.5-6-2 0-3 1-4 1S9 3 7 3z"/></svg></div>
    <div class="feature-label">Kids-Focused<br>Experience</div>
  </div>
  <div class="abs feature" style="left:135px;top:256px">
    <div class="feature-badge"><svg width="22" height="22" viewBox="0 0 24 24" fill="none" stroke="#333" stroke-width="1.4"><path d="M12 2l8 3v6c0 5-3.5 9-8 11-4.5-2-8-6-8-11V5z"/></svg></div>
    <div class="feature-label">Preventive &amp;<br>Comprehensive Care</div>
  </div>
  <div class="abs feature" style="left:242px;top:256px">
    <div class="feature-badge"><svg width="24" height="22" viewBox="0 0 26 24" fill="none" stroke="#333" stroke-width="1.4"><circle cx="8" cy="6" r="3"/><circle cx="18" cy="6" r="3"/><circle cx="13" cy="12" r="2.4"/><path d="M2 20c0-5 3-7 6-7M24 20c0-5-3-7-6-7M8 22c0-3 2-5 5-5s5 2 5 5"/></svg></div>
    <div class="feature-label">Welcoming<br>for the Whole Family</div>
  </div>

  <svg class="abs hero-photo" viewBox="0 0 290 304" role="img" aria-label="Photo of a smiling young girl in a dental chair holding a plush toy">
    <defs><linearGradient id="heroFill" x1="0" y1="0" x2="1" y2="1"><stop offset="0" stop-color="#c9c9c6"/><stop offset=".5" stop-color="#e3b9a0"/><stop offset="1" stop-color="#9fc7d6"/></linearGradient></defs>
    <path d="M60 20 C110 -8 170 10 205 30 C250 50 290 80 282 150 C278 200 250 240 200 270 C150 300 110 300 70 280 C25 255 0 220 6 175 C12 130 25 110 30 80 C35 50 40 30 60 20Z" fill="var(--sage-dark)"/>
    <path d="M72 32 C115 8 170 22 200 42 C240 62 272 90 266 150 C262 195 238 230 195 255 C150 282 115 282 80 265 C40 245 18 212 24 175 C30 135 40 115 45 88 C50 60 55 42 72 32Z" fill="url(#heroFill)" stroke="#fff" stroke-width="3"/>
  </svg>

  <svg class="wave" style="top:330px" width="651" height="91" viewBox="0 0 651 91">
    <path d="M0 12 C50 28 90 28 130 22 C200 10 230 30 270 40 C300 48 320 30 380 22 C460 12 520 30 580 26 C610 24 630 20 651 18 V91 H0Z" fill="var(--cream)"/>
  </svg>

  <div class="contact">
    <div class="pin-ico" style="left:26px;top:10px"><svg width="10" height="10" viewBox="0 0 24 24" fill="#fff"><path d="M6.6 10.8a15 15 0 006.6 6.6l2.2-2.2c.3-.3.7-.4 1-.2 1.1.4 2.3.6 3.6.6.6 0 1 .4 1 1V20c0 .6-.4 1-1 1C10.6 21 3 13.4 3 4c0-.6.4-1 1-1h3.5c.6 0 1 .4 1 1 0 1.3.2 2.5.6 3.6.1.3 0 .7-.2 1z"/></svg></div>
    <div class="phone-num">(555) 014-2386</div>
    <div class="web"><span>hello@maplegrovekids.com</span><span>www.maplegrovekids.com</span></div>
    <div class="pin-ico" style="left:363px;top:10px"><svg width="9" height="10" viewBox="0 0 24 24" fill="#fff"><path d="M12 2a7 7 0 00-7 7c0 5 7 13 7 13s7-8 7-13a7 7 0 00-7-7zm0 9.5A2.5 2.5 0 1112 6a2.5 2.5 0 010 5.5z"/></svg></div>
    <div class="addr">48 Orchard Lane, Suite 210<br>Fairbrook, CT 06000</div>
  </div>
</section>

<!-- BACK -->
<section class="card card-back">
  <div class="abs" role="img" aria-label="Softly faded photo of a bright dental treatment room" style="left:0;top:0;width:651px;height:360px;background:linear-gradient(90deg,rgba(226,214,196,.6),rgba(255,255,255,0) 60%)"></div>

  <div class="abs back-title" style="left:29px;top:31px">Exceptional care.</div>
  <svg class="abs" style="left:218px;top:58px" width="82" height="6" viewBox="0 0 82 6"><path d="M1 4 Q40 1 81 3" stroke="var(--forest)" stroke-width="2" fill="none"/></svg>
  <div class="abs back-sub" style="left:29px;top:68px">For every stage of their smile.</div>
  <p class="abs back-intro" style="left:30px;top:99px;width:340px">At Maple Grove Pediatric Dentistry, we create a positive, stress-free experience where kids feel <em>comfortable</em> and parents feel <em>confident</em>.</p>

  <div class="abs brand-dot" style="left:452px;top:40px;width:26px;height:26px"></div>
  <div class="abs brand-name" style="left:413px;top:85px;width:104px;text-align:center;font-size:17px">maple grove</div>
  <div class="abs brand-tag" style="left:412px;top:105px;width:106px;text-align:center;font-size:6.2px">PEDIATRIC DENTISTRY</div>

  <div class="abs stamp"></div>

  <div class="abs dentist-photo" role="img" aria-label="Portrait photo of the pediatric dentist in a light blue shirt, arms crossed"></div>

  <div class="abs meet" style="left:199px;top:146px">Meet Your<br>Pediatric Dentist</div>
  <div class="abs name-btn"><svg width="14" height="14" viewBox="0 0 24 24" fill="#fff"><path d="M7 3c-3 0-4 3-3.5 6 .5 3 1.5 4 2 8 .3 3 2 3 2.5 0l1-4c.4-1.5 2.6-1.5 3 0l1 4c.5 3 2.2 3 2.5 0 .5-4 1.5-5 2-8 .5-3-.5-6-3.5-6-2 0-3 1-4 1S9 3 7 3z"/></svg>Dr. Owen Hale</div>
  <p class="abs bio">Throughout his own childhood and during his academic and professional career in becoming a pediatric dentist, Dr. Hale has maintained a passion for connecting with others and helping to make a difference in their lives. He is committed to making sure you and your child have a positive and enjoyable experience!</p>

  <svg class="wave" style="top:338px" width="651" height="83" viewBox="0 0 651 83">
    <path d="M0 4 C60 18 120 6 180 16 C260 30 300 24 380 14 C460 4 540 10 651 6 V83 H0Z" fill="var(--cream)"/>
  </svg>

  <div class="contact">
    <div class="pin-ico" style="left:26px;top:10px"><svg width="10" height="10" viewBox="0 0 24 24" fill="#fff"><path d="M6.6 10.8a15 15 0 006.6 6.6l2.2-2.2c.3-.3.7-.4 1-.2 1.1.4 2.3.6 3.6.6.6 0 1 .4 1 1V20c0 .6-.4 1-1 1C10.6 21 3 13.4 3 4c0-.6.4-1 1-1h3.5c.6 0 1 .4 1 1 0 1.3.2 2.5.6 3.6.1.3 0 .7-.2 1z"/></svg></div>
    <div class="phone-num">(555) 014-2386</div>
    <div class="web"><span>hello@maplegrovekids.com</span><span>www.maplegrovekids.com</span></div>
    <div class="pin-ico" style="left:363px;top:10px"><svg width="9" height="10" viewBox="0 0 24 24" fill="#fff"><path d="M12 2a7 7 0 00-7 7c0 5 7 13 7 13s7-8 7-13a7 7 0 00-7-7zm0 9.5A2.5 2.5 0 1112 6a2.5 2.5 0 010 5.5z"/></svg></div>
    <div class="addr">48 Orchard Lane, Suite 210<br>Fairbrook, CT 06000</div>
  </div>
</section>

</body>
</html>
```